Harbourline Service Allies Wordpress Design

See attached brief. If you have questions beyond this please let me know. Brief document is HS Allies Website Design v1. Other documents are files from logo creation and business cards to give you an idea of colours and images. Also see document that shows examples of the types of images I want to display on the website.

Focus of site is for customers and to drive traffic from social media etc. Company is startup consulting business in Customer Experience and Contact Centre. We offer benchmarking, strategy reviews, technology audits. etc

Looking for the site to use the existing Wordpress theme on hostNest or something compatible. Happy to change if there is a good reason for doing so.

Has to be easy to manage ongoing if possible.

Target Market(s)

HSA is a consulting organisation in contact centre and customer experience

Number of Pages Required

4 page

Font styles to use
Serif
Sans Serif

Colors
0255a3
3276b5
33a6d7
0293ce
ffffff
fefdec

Requirements
Must have
• Hosted on hostNest so must be compatible. Preference is to use the theme that is already there (Lumeo) unless there is a reason not to
Nice to have
• see brief

```html
<!DOCTYPE html>
<html lang="en">
<head>
<meta charset="utf-8">
<title>Harbourline Service Allies</title>
<link rel="stylesheet" href="https://fonts.googleapis.com/css2?family=Open+Sans:wght@400;600;700&family=Roboto:wght@300;400&display=swap">
<style>
:root{
  --navy:#0a4a8c;
  --blue:#0255a3;
  --mid-blue:#3276b5;
  --sky:#0293ce;
  --bright:#0aa6e6;
  --cyan:#33a6d7;
  --ink:#2e2e2e;
  --grey-text:#8a8a8a;
  --page:#f3f2f5;
  --white:#ffffff;
  --dark:#333333;
}
*{margin:0;padding:0;box-sizing:border-box}
html,body{width:1200px;height:3321px;overflow:hidden}
body{position:relative;background:var(--page);font-family:"Open Sans",Arial,sans-serif;color:var(--ink)}
.abs{position:absolute}

/* top strip */
.top-strip{left:0;top:0;width:1200px;height:40px;background:var(--white);border-top:4px solid var(--sky);border-bottom:1px solid #d8d8d8}
.social{left:930px;top:8px;display:flex;gap:6px}
.social span{width:27px;height:27px;border-radius:50%;background:var(--blue);border:2px solid #cfd9e6}

/* header */
.header{left:0;top:40px;width:1200px;height:133px;background:var(--page)}
.nav-item{top:94px;font-size:14px;color:#444}
.nav-home{left:142px;top:44px;width:82px;height:126px;background:var(--navy);color:var(--white);font-size:14px;font-weight:700;display:flex;align-items:center;justify-content:center}
.brand{left:470px;top:66px;width:260px;text-align:center;display:flex;flex-direction:column;align-items:center;gap:6px}
.brand-mark{width:38px;height:38px;border-radius:50%;background:var(--sky)}
.brand-name{font-family:"Open Sans",Arial,sans-serif;font-weight:700;font-size:16px;color:var(--navy);line-height:1.15}

/* hero */
.hero{left:0;top:173px;width:1200px;height:591px;background:linear-gradient(90deg,#e8e8e8 0%,#d9d9d9 40%,#c9c9c9 75%,#9a9a9a 100%)}
.hero-caption{left:244px;top:354px;width:673px;height:182px;background:rgba(40,80,130,.55);color:var(--white);text-align:center;font-family:"Roboto",Arial,sans-serif;padding-top:16px}
.hero-caption h1{font-weight:300;font-size:40px;line-height:48px;text-transform:uppercase}
.hero-caption p{font-size:17px;margin-top:12px;opacity:.9}
.arrow{top:436px;width:46px;height:47px;background:var(--sky);display:flex;align-items:center;justify-content:center}
.dots{left:568px;top:716px;display:flex;gap:8px}
.dots span{width:12px;height:12px;border-radius:50%;background:rgba(255,255,255,.7)}
.hero-shadow{left:0;top:764px;width:1200px;height:50px;background:radial-gradient(ellipse at top,rgba(0,0,0,.18),rgba(0,0,0,0) 70%)}

/* welcome */
.welcome{left:0;top:870px;width:1200px;text-align:center;font-family:"Roboto",Arial,sans-serif;font-weight:300;font-size:47px;color:#333}
.ask{left:100px;top:1018px;display:flex;flex-direction:column;gap:8px}
.ask span{display:inline-block;background:var(--navy);color:var(--white);font-size:36px;line-height:46px;padding:0 12px;align-self:flex-start}
.ask-icon{left:500px;top:1018px;width:200px;height:200px;border-radius:50%;background:#e3e3e6}
.intro{left:786px;top:1018px;width:322px;font-size:13px;line-height:22px;color:var(--grey-text)}
.btn-outline{left:786px;top:1193px;width:162px;height:54px;border:2px solid var(--navy);color:var(--navy);font-size:17px;display:flex;align-items:center;justify-content:center}

/* services */
.services-photo{left:0;top:1289px;width:591px;height:662px;background:linear-gradient(135deg,#c8b6a4 0%,#e6d9cf 40%,#b9a79a 70%,#8d8a88 100%)}
.services-panel{left:591px;top:1289px;width:609px;height:662px;background:linear-gradient(180deg,#404042 0%,#2d2d2f 100%);color:var(--white)}
.services-panel h2{position:absolute;left:47px;top:32px;font-weight:400;font-size:31px}
.services-panel .lead{position:absolute;left:47px;top:88px;width:520px;font-size:13px;line-height:20px}
.service{position:absolute;left:58px;width:520px;display:flex;gap:18px}
.service h3{font-size:18px;font-weight:600;line-height:22px}
.service p{font-size:12.5px;line-height:18px;width:415px}
.btn-ghost{position:absolute;left:206px;top:560px;width:113px;height:40px;border:2px solid #ddd;font-size:13px;display:flex;align-items:center;justify-content:center}

/* projects */
.projects-title{left:0;top:2005px;width:1200px;text-align:center;font-weight:700;font-size:24px;color:#222}
.project{top:2072px;width:258px;text-align:center}
.project-photo{height:147px;width:258px}
.project h4{font-size:14px;font-weight:700;color:#333;margin-top:34px;letter-spacing:.3px}
.project p{font-size:12px;line-height:17px;color:var(--grey-text);margin-top:14px}
.btn-solid{display:inline-block;margin-top:18px;width:93px;height:36px;background:var(--navy);color:var(--white);font-size:13px;font-weight:600;line-height:36px}

/* band */
.band{left:0;top:2475px;width:1200px;height:111px;background:var(--navy)}
.band p{position:absolute;left:99px;top:42px;color:var(--white);font-weight:700;font-size:20px}
.band .btn-dark{position:absolute;left:826px;top:40px;width:146px;height:38px;background:var(--dark);color:var(--white);font-size:12px;font-weight:700;display:flex;align-items:center;justify-content:center}

/* contact */
.contact-bg{left:0;top:2586px;width:609px;height:664px;background:linear-gradient(180deg,#4a4641 0%,#5a5650 45%,#3f3d3a 100%)}
.contact-photo{left:609px;top:2586px;width:591px;height:664px;background:linear-gradient(180deg,#c9c7bf 0%,#b3b2ab 55%,#8f8e88 100%)}
.contact-title{left:97px;top:2672px;color:var(--white);font-size:33px;font-weight:400}
.field{left:97px;width:390px;height:47px;background:rgba(160,160,160,.5);color:var(--white);font-size:14px;display:flex;align-items:center;justify-content:space-between;padding:0 16px}
.field.msg{height:144px;align-items:flex-start;padding-top:14px}
.send{left:352px;top:3111px;width:135px;height:44px;background:var(--bright);color:var(--white);font-size:14px;display:flex;align-items:center;justify-content:center}

/* footer */
.footer{left:0;top:3250px;width:1200px;height:71px;background:var(--navy);color:#dfe8f3;font-size:12px}
.footer p{position:absolute;left:104px;top:27px}
.footer em{font-style:normal;color:var(--cyan)}
</style>
</head>
<body>

<div class="abs top-strip"></div>
<div class="abs social" aria-label="Social links"><span></span><span></span><span></span><span></span><span></span></div>

<header class="abs header"></header>
<div class="abs nav-home">Home</div>
<div class="abs nav-item" style="left:248px">About Us</div>
<div class="abs nav-item" style="left:358px">Partners</div>
<div class="abs brand">
  <span class="brand-mark"></span>
  <span class="brand-name">Harbourline Service Allies</span>
</div>
<div class="abs nav-item" style="left:795px">Services</div>
<div class="abs nav-item" style="left:897px">Blog</div>
<div class="abs nav-item" style="left:973px">Contact Us</div>

<section class="abs hero" role="img" aria-label="Hand moving a black chess king across a board of pawns"></section>
<div class="abs hero-caption">
  <h1>Our best services<br>for best clients</h1>
  <p>Emergent eradicate, medical supplies assistance, education pride challenges of our times.</p>
</div>
<div class="abs arrow" style="left:0">
  <svg width="14" height="22" viewBox="0 0 14 22"><path d="M11 2 3 11l8 9" fill="none" stroke="#fff" stroke-width="3"/></svg>
</div>
<div class="abs arrow" style="left:1154px">
  <svg width="14" height="22" viewBox="0 0 14 22"><path d="M3 2l8 9-8 9" fill="none" stroke="#fff" stroke-width="3"/></svg>
</div>
<div class="abs dots"><span></span><span></span><span></span></div>
<div class="abs hero-shadow"></div>

<h2 class="abs welcome">Welcome to our company!</h2>

<div class="abs ask"><span>Ask professionals</span><span>for a business</span><span>advice!</span></div>
<div class="abs ask-icon">
  <svg width="200" height="200" viewBox="0 0 200 200">
    <circle cx="100" cy="78" r="30" fill="none" stroke="#333" stroke-width="5"/>
    <ellipse cx="100" cy="78" rx="13" ry="30" fill="none" stroke="#333" stroke-width="4"/>
    <path d="M70 78h60M75 62h50M75 94h50" stroke="#333" stroke-width="4"/>
    <circle cx="64" cy="112" r="11" fill="#333"/>
    <circle cx="136" cy="112" r="11" fill="#333"/>
    <path d="M44 150c0-18 9-26 20-26s20 8 20 26zM116 150c0-18 9-26 20-26s20 8 20 26z" fill="#333"/>
  </svg>
</div>
<p class="abs intro">Nemo enim ipsam voluptatem quia voluptas sit aspernatur aut odit aut fugit quia consequuntur magni dolores eos qui ratione voluptatem sequi nesciunt. Neque porro quisquam est, qui dolorem ipsum quia dolor sit amet, consectetur, adipisci velit, sed quia non numquam eius modi.</p>
<div class="abs btn-outline">Learn more</div>

<div class="abs services-photo" role="img" aria-label="Two colleagues smiling while working together at a desk"></div>
<section class="abs services-panel">
  <h2>Services</h2>
  <p class="lead">Fem vel eum iriure dolor in hendrerit in vulputate velit esse molestie consequat, vel illum dolore eu feugiat nulla facilisis at vero</p>
  <div class="service" style="top:160px">
    <svg width="72" height="60" viewBox="0 0 72 60"><circle cx="36" cy="18" r="10" fill="#33a6d7"/><circle cx="16" cy="24" r="8" fill="#33a6d7"/><circle cx="56" cy="24" r="8" fill="#33a6d7"/><path d="M18 52c0-14 8-22 18-22s18 8 18 22zM2 52c0-10 6-16 14-16 4 0 7 1 9 3-4 4-6 8-7 13zM70 52c0-10-6-16-14-16-4 0-7 1-9 3 4 4 6 8 7 13z" fill="#33a6d7"/></svg>
    <div><h3 style="color:var(--cyan)">Support</h3><p>Fem vel eum iriure dolor in hendrerit in vulputate velit esse molestie consequat, vel illum dolore eu feugiat nulla facilisis</p></div>
  </div>
  <div class="service" style="top:288px">
    <svg width="72" height="60" viewBox="0 0 72 60"><rect x="6" y="4" width="60" height="52" fill="none" stroke="#fff" stroke-width="4"/><path d="M6 20h60M6 38h60" stroke="#fff" stroke-width="3"/><g fill="#fff"><circle cx="20" cy="12" r="4"/><circle cx="30" cy="12" r="4"/><circle cx="50" cy="29" r="4"/><circle cx="22" cy="29" r="4"/><circle cx="40" cy="47" r="4"/><circle cx="52" cy="47" r="4"/></g></svg>
    <div><h3>Finance &amp; Accounting</h3><p>Fem vel eum iriure dolor in hendrerit in vulputate velit esse molestie consequat, vel illum dolore eu feugiat nulla facilisis</p></div>
  </div>
  <div class="service" style="top:416px">
    <svg width="72" height="64" viewBox="0 0 72 64"><g fill="#fff"><ellipse cx="20" cy="10" rx="14" ry="5"/><rect x="6" y="10" width="28" height="14"/><ellipse cx="46" cy="40" rx="14" ry="5"/><rect x="32" y="40" width="28" height="18"/><ellipse cx="20" cy="44" rx="12" ry="4"/><rect x="8" y="44" width="24" height="12"/></g><path d="M40 14h16v16M52 26l4 4 4-4" fill="none" stroke="#fff" stroke-width="3"/></svg>
    <div><h3>Management</h3><p>Fem vel eum iriure dolor in hendrerit in vulputate velit esse molestie consequat, vel illum dolore eu feugiat nulla facilisis</p></div>
  </div>
  <div class="btn-ghost">View More</div>
</section>

<h2 class="abs projects-title">LATEST PROJECTS</h2>
<article class="abs project" style="left:195px">
  <div class="project-photo" role="img" aria-label="Businessman drawing a pulse line on a glass board" style="background:linear-gradient(90deg,#f2f2f2,#d8d8d8)"></div>
  <h4>PROIN ID VELIT LOBORTIS</h4>
  <p>Lorem ipsum dolor sit amet, consectetur alle adiping elit. Etiam metus libero, lacinia sedrt erat allet ritos avoised.</p>
  <span class="btn-solid">Read More</span>
</article>
<article class="abs project" style="left:472px">
  <div class="project-photo" role="img" aria-label="Two business people shaking hands over a desk" style="background:linear-gradient(135deg,#1f3f66,#7d95b0,#2a4a72)"></div>
  <h4>QUISQUE UT EROS MAGNA</h4>
  <p>Lorem ipsum dolor sit amet, consectetur alle adiping elit. Etiam metus libero, lacinia sedrt erat allet ritos avoised.</p>
  <span class="btn-solid">Read More</span>
</article>
<article class="abs project" style="left:746px">
  <div class="project-photo" role="img" aria-label="Young man with a laptop and glowing idea graphics" style="background:linear-gradient(90deg,#cfe3f0,#9fc3df,#dbe9f3)"></div>
  <h4>PROIN ID VELIT LOBORTIS</h4>
  <p>Lorem ipsum dolor sit amet, consectetur alle adiping elit. Etiam metus libero, lacinia sedrt erat allet ritos avoised.</p>
  <span class="btn-solid">Read More</span>
</article>

<section class="abs band">
  <p>SAVE TIME, SAVE MONEY, GROW &amp; SUCCEED!</p>
  <span class="btn-dark">More</span>
</section>

<div class="abs contact-bg" role="img" aria-label="Dark misty landscape behind the contact form"></div>
<div class="abs contact-photo" role="img" aria-label="Businessman on a ladder looking through binoculars into a hazy sky"></div>
<h2 class="abs contact-title">Contact Form</h2>
<div class="abs field" style="top:2752px">Name
  <svg width="20" height="22" viewBox="0 0 20 22"><circle cx="10" cy="6" r="5" fill="#fff"/><path d="M1 21c0-7 4-10 9-10s9 3 9 10z" fill="#fff"/></svg></div>
<div class="abs field" style="top:2816px">Phone
  <svg width="20" height="20" viewBox="0 0 20 20"><path d="M4 1l4 4-2 3c1 3 3 5 6 6l3-2 4 4-3 3C8 19 1 12 1 4z" fill="#fff"/></svg></div>
<div class="abs field" style="top:2878px">Email
  <svg width="22" height="16" viewBox="0 0 22 16"><rect x="1" y="1" width="20" height="14" fill="none" stroke="#fff" stroke-width="2"/><path d="M1 1l10 8 10-8" fill="none" stroke="#fff" stroke-width="2"/></svg></div>
<div class="abs field msg" style="top:2940px">Message
  <svg width="18" height="18" viewBox="0 0 18 18"><path d="M2 16l1-5L13 1l4 4L7 15z" fill="#fff"/></svg></div>
<div class="abs send">SEND</div>

<footer class="abs footer"><p>Copyright 2015 &nbsp;|&nbsp; All Rights Reserved &nbsp;|&nbsp; Powered by <em>Lumeo</em></p></footer>

</body>
</html>
```